Business Card and Logo Color Scheme Design Contest

We are starting a new company called Lone Ridge Structural Partners and already have a logo however, the colors for the logo itself are not final and COULD be changed. I'm hoping to move AWAYfrom the gold color in the card and the logo as it seems a bit outdated. What we need help with is to find what our business color scheme will be, and then incorporate those colors into both the logo and the business card design itself. We also want to make sure we are known as "LRS" so in the future we can just refer to ourselves as "LRS" and not Lone Ridge Structural Partners. That being said, I would like to make a slight change to the logo to somehow include the letters "LRS." The logo used in the front of the card design MUST ALSO include the words "Firm No. 64307" within the logo. My vision is for the front of the card to have the information shown in the attached image. For the back of the card, I'm hoping to have something very simple. I'm envisioning a solid color with either the website (www.bridgemarkplans.com) and a simplified version of the logo. I've attached an example but I'm looking for a complete redesign. I'm looking for a slick, modern and simple design.

Industry/Entity Type

Civil Engineer

Contact Information for Business Card

Logo
Firm No. 64307
Marcus Holloway, PE
Chief Operating Officer
Email:mholloway@bridgemarkplans.com
Ph: 936.555.0142 | D: 936.555.0178 | M:210.555.0263
4187 W. Kellingham, Conroe, Texas 77301
www.bridgemarkplans.com

Requirements
Must have
• Logo
Contact Info
Nice to have
• "LRS" Incorporated in the design
Should not have
• The current color scheme

```html
<!DOCTYPE html>
<html lang="en">
<head>
<meta charset="utf-8">
<title>Lone Ridge Structural Partners — Business Card</title>
<link rel="stylesheet" href="https://fonts.googleapis.com/css2?family=Open+Sans:wght@400;600&family=Source+Sans+3:wght@400&family=Marcellus&display=swap">
<style>
  :root {
    --page: #d8d8d8;
    --card-dark: #2a2a2a;
    --panel-dark: #2c2c2c;
    --frame-dark: #474747;
    --mark-grey: #929292;
    --url-grey: #6a6a6a;
    --marble-light: #fbfbfb;
    --marble-vein: #ececec;
    --frame-light: #505050;
    --ink: #2b2b2b;
    --ink-soft: #777777;
    --logo-text: #e8e2d6;
    --logo-rule: #8a8a8a;
  }
  * { margin: 0; padding: 0; box-sizing: border-box; }
  html, body { width: 1200px; height: 1200px; overflow: hidden; background: var(--page); }
  .canvas { position: relative; width: 1200px; height: 1200px; }

  .card {
    position: absolute; left: 237px; width: 674px;
    box-shadow: 0 10px 22px rgba(0,0,0,0.22);
    overflow: hidden;
  }
  .card-back { top: 191px; height: 391px; background: var(--card-dark); }
  .card-front { top: 694px; height: 409px; }

  .frame { position: absolute; inset: 17px; border: 1.5px solid var(--frame-dark); }
  .card-front .frame { border: 2px solid var(--frame-light); }

  .back-panel {
    position: absolute; left: 192px; top: 9px; width: 294px; bottom: 0;
    background: var(--panel-dark);
  }
  .back-monogram {
    position: absolute; left: 0; right: 0; top: 115px; text-align: center;
    font-family: "Marcellus", serif; font-size: 64px; letter-spacing: 4px;
    color: var(--mark-grey);
  }
  .back-url {
    position: absolute; left: 0; right: 0; top: 349px; text-align: center;
    font-family: "Source Sans 3", sans-serif; font-size: 11px; letter-spacing: 3px;
    color: var(--url-grey); text-transform: uppercase;
  }

  .marble {
    position: absolute; inset: 0;
    background:
      radial-gradient(ellipse at 30% 20%, var(--marble-vein) 0%, transparent 45%),
      radial-gradient(ellipse at 75% 70%, var(--marble-vein) 0%, transparent 50%),
      var(--marble-light);
  }
  .logo-block {
    position: absolute; left: 53px; top: 0; width: 250px; height: 248px;
    background: var(--card-dark);
    display: flex; flex-direction: column; align-items: center; justify-content: center; text-align: center;
  }
  .logo-name {
    font-family: "Open Sans", sans-serif; font-weight: 600; font-size: 18px;
    line-height: 1.3; letter-spacing: 1px; color: var(--logo-text); text-transform: uppercase;
  }
  .logo-rule { width: 150px; height: 1px; background: var(--logo-rule); margin: 12px 0 10px; }
  .logo-firm {
    font-family: "Open Sans", sans-serif; font-weight: 600; font-size: 12px;
    letter-spacing: 2px; color: var(--logo-text); text-transform: uppercase;
  }
  .person { position: absolute; left: 53px; top: 273px; font-family: "Open Sans", sans-serif; color: var(--ink); }
  .person-name { font-size: 23px; letter-spacing: 1.5px; line-height: 1; white-space: nowrap; }
  .person-title { font-size: 15px; letter-spacing: 1.6px; margin-top: 8px; white-space: nowrap; }
  .rule { position: absolute; left: 53px; top: 343px; width: 31px; height: 3px; background: var(--ink); }

  .contact, .address {
    position: absolute; left: 401px; font-family: "Source Sans 3", sans-serif;
    font-size: 15.5px; line-height: 20px; color: var(--ink-soft); white-space: nowrap;
  }
  .contact { top: 118px; }
  .address { top: 274px; }
  .address .street-number { color: var(--ink); }
</style>
</head>
<body>
<main class="canvas">
  <section class="card card-back" aria-label="Card back">
    <div class="frame"></div>
    <div class="back-panel">
      <div class="back-monogram">LRS</div>
      <div class="back-url">www.bridgemarkplans.com</div>
    </div>
  </section>

  <section class="card card-front" aria-label="Card front">
    <div class="marble" role="img" aria-label="White marble texture background"></div>
    <div class="frame"></div>
    <div class="logo-block">
      <div class="logo-name">Lone Ridge<br>Structural Partners</div>
      <div class="logo-rule"></div>
      <div class="logo-firm">Firm No. 64307</div>
    </div>
    <div class="person">
      <div class="person-name">MARCUS HOLLOWAY, PE</div>
      <div class="person-title">CHIEF OPERATING OFFICER</div>
    </div>
    <div class="rule"></div>
    <div class="contact">
      E. mholloway@bridgemarkplans.com<br>
      P. 936.555.0142<br>
      D: 936.555.0178<br>
      M: 210.555.0263
    </div>
    <div class="address">
      <span class="street-number">4187 W.</span> Kellingham,<br>
      Conroe, Texas<br>
      77301
    </div>
  </section>
</main>
</body>
</html>
```